Yoga class opening. Little schedule for JUNE JULY and AUGUST

Flyer to promote an opening yoga class. The color of the docx haven't to be respected.

We want something joyfull, professional, clean and serious.

About the logo we oppened a contest at the same time so at the moment there is no logo but the logo color will be simple.

The phone number will change so you can poste a random one for the design that i can change by myself.

i recieved many creation in both side BUT i want something in 1 side :)

Yoga student. all age

It Professional

Yoga brook

Sans Serif

• The text present on the docx
• Some symbols about yoga ( Namasté signs, mandala, ... )
• Not too much details it has to be clear.

```html
<!DOCTYPE html>
<html lang="fr">
<head>
<meta charset="utf-8">
<title>Yoga brook – Stages d'été</title>
<link rel="stylesheet" href="https://fonts.googleapis.com/css2?family=Cinzel:wght@400;700&family=Roboto+Condensed:ital,wght@0,400;0,700;1,400&family=Lora:wght@500&family=Kaushan+Script&display=swap">
<style>
:root{
  --plum:#7a1f52;
  --plum-dark:#5e153e;
  --sun:#f7c51a;
  --tangerine:#e8731c;
  --bark:#2e1d10;
  --tan:#8b6a45;
  --cream:#fdf5e8;
  --cream-alt:#fbe6c4;
  --row-text:#3a2a1a;
  --paper:#f6f4f3;
  --white:#ffffff;
}
*{margin:0;padding:0;box-sizing:border-box}
html,body{width:848px;height:1200px;overflow:hidden;background:var(--white)}
.flyer{position:relative;width:848px;height:1200px;overflow:hidden;background:var(--paper);font-family:"Roboto Condensed",sans-serif}
.hero-photo{position:absolute;left:0;top:0;width:848px;height:300px;background:linear-gradient(180deg,#2f7fd6 0%,#7ab7ec 55%,#6c9a4e 100%)}
.waves{position:absolute;left:0;top:0}
.headline{position:absolute;left:36px;top:228px;color:var(--white);font-family:"Cinzel",serif}
.headline .kicker{font-size:38px;font-weight:700;line-height:1}
.headline .brand{font-size:58px;font-weight:700;color:var(--sun);line-height:1.05;margin-top:2px}
.headline .line{font-size:26px;line-height:1.25}
.headline .line em{font-style:normal;color:var(--sun);font-size:31px;font-weight:700}
.headline .address{font-size:17px;margin-top:4px;font-variant:small-caps;letter-spacing:.3px}
.waiting{position:absolute;left:492px;top:432px;color:var(--white);font-style:italic;font-size:22px;line-height:1.06;width:150px}
.summer-cloud{position:absolute;left:626px;top:428px;width:222px;height:132px;background:var(--sun);border-radius:60px 40px 50px 70px}
.summer-cloud p{position:absolute;left:38px;top:26px;color:var(--plum);font-family:"Kaushan Script",cursive;transform:rotate(-5deg);line-height:1}
.summer-cloud .brand{font-size:30px}
.summer-cloud .tagline{font-size:16px;margin-top:4px}
.mandala{position:absolute;left:370px;top:473px;width:102px;height:102px;border-radius:50%;background:var(--white);border:2px solid var(--plum);display:flex;align-items:center;justify-content:center}
.mandala span{display:block;width:70px;height:70px;border-radius:50%;background:radial-gradient(circle,#555 0%,#999 45%,#ddd 70%,#fff 100%)}

.month-tag{position:absolute;height:28px;border-radius:14px;background:var(--bark);color:var(--white);font-size:19px;font-weight:700;display:flex;align-items:center;padding-left:12px;gap:6px}
.month-tag i{display:inline-block;width:14px;height:8px;border-radius:0 0 8px 8px;background:var(--white)}
.price-tag{position:absolute;height:28px;border-radius:14px;background:var(--bark);color:var(--white);font-size:19px;font-weight:700;display:flex;align-items:center;justify-content:center}
.price-tag b{color:var(--sun)}
.schedule{position:absolute;border:1px solid #e3c9a0;background:var(--cream);z-index:2}
.schedule h3{background:var(--tan);color:var(--white);font-family:"Lora",serif;font-weight:500;font-size:17px;height:29px;line-height:29px;padding-left:16px}
.schedule li{list-style:none;height:19.5px;line-height:19.5px;font-size:12.3px;color:var(--row-text);padding-left:12px}
.schedule li:nth-child(even){background:var(--cream-alt)}

.stretch-photo{position:absolute;left:462px;top:850px;width:386px;height:208px;z-index:1;background:linear-gradient(100deg,rgba(246,244,243,0) 0%,#efe6dc 25%,#e9cfc0 60%,#e4587a 85%,#f3dede 100%)}
.season-band{position:absolute;left:0;top:1058px;width:848px;height:38px;background:var(--plum);color:var(--white);font-size:27px;text-align:center;line-height:38px}
.season-band b{color:var(--sun);font-weight:700}
.contact{position:absolute;left:45px;top:1104px;color:#2f2f2f;font-style:italic;font-size:13.5px;line-height:18px}
.contact h4{color:var(--tangerine);font-size:19px;font-weight:700;font-style:italic;margin-bottom:2px}
.contact p{display:flex;align-items:center;gap:6px}
.contact svg{flex:none}
.contact .page{color:var(--plum);font-style:normal}
.farewell{position:absolute;left:425px;top:1118px;color:var(--plum);font-family:"Kaushan Script",cursive;font-size:40px;transform:rotate(-2deg)}
.farewell::after{content:"";display:block;width:160px;height:3px;background:var(--plum);margin:-4px 0 0 230px;border-radius:2px}
</style>
</head>
<body>
<main class="flyer">
  <div class="hero-photo" role="img" aria-label="Photo d'un groupe en méditation assis en tailleur au bord d'un lac, ciel bleu"></div>

  <svg class="waves" width="848" height="640" viewBox="0 0 848 640" aria-hidden="true">
    <path d="M0,140 C220,150 520,250 848,280 L848,290 C520,265 220,165 0,158 Z" fill="#fff"/>
    <path d="M0,160 C220,170 520,270 848,300 L848,600 C660,612 520,592 420,585 C300,578 120,518 0,528 Z" fill="var(--plum)"/>
    <path d="M0,521 C170,478 320,552 440,552 C590,552 700,460 848,334" fill="none" stroke="#fff" stroke-width="5"/>
    <path d="M0,513 C170,470 320,540 440,540 C590,540 700,450 848,325" fill="none" stroke="var(--sun)" stroke-width="14"/>
    <path d="M0,556 C180,520 320,565 440,565 C600,565 730,480 848,368" fill="none" stroke="var(--tangerine)" stroke-width="18"/>
    <path d="M0,574 C180,540 320,584 440,584 C600,584 735,500 848,392" fill="none" stroke="#fff" stroke-width="4"/>
  </svg>

  <header class="headline">
    <p class="kicker">NOUVEAU !</p>
    <h1 class="brand">YOGA BROOK</h1>
    <p class="line">VOTRE STUDIO DE YOGA A <em>IXELLES</em></p>
    <p class="line">OUVERTURE LE 6 JUIN 2016 AU</p>
    <p class="address">212 Rue des Tilleuls 1050 Ixelles</p>
  </header>

  <p class="waiting">En attendant le planning des cours de la rentrée</p>
  <div class="summer-cloud">
    <p><span class="brand">YOGA BROOK</span><br><span class="tagline">vous propose ses<br>stages et ateliers d'été.</span></p>
  </div>
  <div class="mandala" role="img" aria-label="Mandala décoratif"><span></span></div>

  <div class="month-tag" style="left:50px;top:586px;width:100px"><i></i>JUIN</div>
  <div class="price-tag" style="left:280px;top:586px;width:110px">10h/<b>85€</b></div>
  <section class="schedule" style="left:50px;top:619px;width:349px">
    <h3>Stage découverte du YOGA</h3>
    <ul>
      <li>Du lundi 6 au vendredi 10 juin : 10h00 à 12h00 ou 18h00 à 20h00</li>
      <li>Du lundi 13 au vendredi 17 juin : 10h00 à 12h00 ou 18h00 à 20h00</li>
      <li>Du lundi 20 au vendredi 24 juin : 10h00 à 12h00 ou 18h00 à 20h00</li>
      <li>Du lundi 27 au vendredi 1er juillet : 10h00 à 12h00 ou 18h00 à 20h00</li>
    </ul>
  </section>

  <div class="price-tag" style="left:691px;top:624px;width:111px">2h/<b>28 €</b></div>
  <section class="schedule" style="left:413px;top:658px;width:386px">
    <h3>Atelier gestion du stress yoga/sophrologie</h3>
    <ul>
      <li>Samedi 11 juin 10h30 à 12h30 OR 15h00 à 17h00</li>
      <li>Dimanche 12 juin 10h30 à 12h30 OR 14h à 16h00</li>
    </ul>
  </section>

  <div class="month-tag" style="left:50px;top:742px;width:116px"><i></i>JUILLET</div>
  <div class="price-tag" style="left:275px;top:742px;width:116px">10h/<b>85€</b></div>
  <section class="schedule" style="left:50px;top:774px;width:349px">
    <h3>Stage initiation à l'ASHTANGA</h3>
    <ul>
      <li>Du lundi 4 au vendredi 8 juillet : 10h00 à 12h00 ou 18h00 à 20h00</li>
      <li>Du lundi 11 au vendredi 15 juillet : 10h00 à 12h00 ou 18h00 à 20h00</li>
      <li>Du lundi 18 au vendredi 22 juillet : 10h00 à 12h00 ou 18h00 à 20h00</li>
      <li>Du lundi 25 au vendredi 29 juillet : 10h00 à 12h00 ou 18h00 à 20h00</li>
    </ul>
  </section>

  <div class="price-tag" style="left:688px;top:740px;width:111px">2h/<b>28€</b></div>
  <section class="schedule" style="left:413px;top:774px;width:386px">
    <h3>Atelier gestion du stress yoga/sophrologie</h3>
    <ul>
      <li>Samedi 9 juillet 10h30 à 12h30 OR 15h00 à 17h00</li>
      <li>Dimanche 10 juillet 10h30 à 12h30 OR 14h00 à 16h00</li>
    </ul>
  </section>

  <div class="stretch-photo" role="img" aria-label="Photo de deux femmes en posture d'étirement assis"></div>

  <div class="month-tag" style="left:47px;top:898px;width:119px"><i></i>AOUT</div>
  <div class="price-tag" style="left:274px;top:898px;width:117px">10h/<b>85€</b></div>
  <section class="schedule" style="left:50px;top:930px;width:349px">
    <h3>Stage découverte du YOGA</h3>
    <ul>
      <li>Du lundi 1er au vendredi 5 août : 10h00 à 12h00 ou 18h00 à 20h00</li>
      <li>Du lundi 8 au vendredi 12 août: 10h00 à 12h00 ou 18h00 à 20h00</li>
      <li>Du lundi 15 au vendredi 19 août: 10h00 à 12h00 ou 18h00 à 20h00</li>
      <li>Du lundi 22 au vendredi 26août: 10h00 à 12h00 ou 18h00 à 20h00</li>
    </ul>
  </section>

  <p class="season-band">Démarrage du planning annuel le <b>5 septembre 2016</b></p>

  <footer class="contact">
    <h4>Plus d'info et inscription :</h4>
    <p><svg width="11" height="11" viewBox="0 0 24 24"><path d="M6.6 10.8a15 15 0 0 0 6.6 6.6l2.2-2.2c.3-.3.7-.4 1-.2 1.1.4 2.3.6 3.6.6.6 0 1 .4 1 1V20c0 .6-.4 1-1 1A17 17 0 0 1 3 4c0-.6.4-1 1-1h3.5c.6 0 1 .4 1 1 0 1.3.2 2.5.6 3.6.1.3 0 .7-.2 1z" fill="var(--tangerine)"/></svg>04 70 00 12 34</p>
    <p><svg width="11" height="9" viewBox="0 0 22 16"><rect x="1" y="1" width="20" height="14" fill="none" stroke="var(--tangerine)" stroke-width="2"/><path d="M1 1l10 8 10-8" fill="none" stroke="var(--tangerine)" stroke-width="2"/></svg>yogabrookixelles@mailbox.be</p>
    <p>Ou via notre page Linkfeed : <span class="page">yoga brook</span></p>
  </footer>

  <p class="farewell">UN BEL ETE A TOUS !</p>
</main>
</body>
</html>
```